Bref créative
Business Card for ecommerce technology company
Circuitry Supply Partners, LLC.
Professional
Paul Dunmore
President
457 Ridgeback Ave.
Fernvale, QX 58204
mark@quorvix.com
www.quorvix.com
Please send Business card so I will be able to edit it for other employees

```html
<!DOCTYPE html>
<html lang="en">
<head>
<meta charset="utf-8">
<title>Quorvix Stationery</title>
<link href="https://fonts.googleapis.com/css2?family=Exo+2:wght@400;600;800&display=swap" rel="stylesheet">
<style>
:root{
  --bg:#eef1f4;
  --paper:#ffffff;
  --blue:#1f63d6;
  --blue-deep:#0b3f9e;
  --blue-light:#4a8df0;
  --ink:#2a2f38;
  --muted:#6b7380;
  --line:#1c2230;
}
*{margin:0;padding:0;box-sizing:border-box}
html,body{width:1200px;height:936px;overflow:hidden;background:var(--bg);font-family:"Exo 2",Arial,sans-serif;color:var(--ink)}
.canvas{position:relative;width:1200px;height:936px}
.sheet{position:absolute;background:var(--paper);box-shadow:0 4px 14px rgba(0,0,0,.18);overflow:hidden}
.band{position:absolute;left:0;bottom:0;width:100%}
.band-text{position:absolute;left:0;width:100%;text-align:center;color:#fff;letter-spacing:4px;font-weight:600}
.mark{display:flex;align-items:center;gap:8px;color:var(--blue);font-weight:800}
.mark-dot{border-radius:50%;background:var(--blue);flex:none}

/* letterhead */
.letterhead{left:184px;top:72px;width:430px;height:563px}
.letterhead .mark{position:absolute;left:26px;top:26px;font-size:26px}
.letterhead .mark-dot{width:42px;height:42px}
.letterhead .tagline{position:absolute;left:76px;top:60px;font-size:8px;color:var(--muted)}
.contact-list{position:absolute;left:290px;top:24px;list-style:none;font-size:8px;line-height:15px;color:var(--muted)}
.contact-list li{display:flex;align-items:center;gap:5px}
.contact-list i{width:7px;height:7px;border-radius:50%;background:var(--blue);display:inline-block}
.watermark{position:absolute;left:150px;top:235px;width:130px;height:130px;border-radius:50%;background:var(--blue-light);opacity:.12}
.letterhead .band-text{bottom:14px;font-size:9px}

/* folder */
.folder{left:640px;top:51px;width:425px;height:609px}
.folder .emblem{position:absolute;left:145px;top:160px;width:135px;height:135px;border-radius:50%;background:var(--blue)}
.folder .name{position:absolute;left:0;top:300px;width:100%;text-align:center;font-size:44px;font-weight:800;color:var(--blue);letter-spacing:1px}
.folder .tagline{position:absolute;left:0;top:356px;width:100%;text-align:center;font-size:14px;color:var(--muted)}
.folder .band-text{bottom:16px;font-size:10px}

/* business cards */
.card{left:41px;width:215px;height:108px}
.card-front{top:660px}
.card-back{top:786px}
.card-front .mark{position:absolute;left:10px;top:8px;font-size:14px;gap:5px}
.card-front .mark-dot{width:18px;height:18px}
.person{position:absolute;left:12px;top:40px;font-size:7px;color:var(--muted);line-height:10px}
.person strong{display:block;color:var(--ink);font-size:8px}
.card-contact{position:absolute;left:110px;top:34px;font-size:6px;line-height:9px;color:var(--muted)}
.card-front .band-text,.card-back .band-text{bottom:5px;font-size:6px;letter-spacing:2px}
.card-back .emblem{position:absolute;left:84px;top:22px;width:46px;height:46px;border-radius:50%;background:var(--blue)}

/* envelopes */
.envelope{left:264px;top:670px;width:440px;height:213px}
.envelope .mark{position:absolute;left:20px;top:18px;font-size:20px}
.envelope .mark-dot{width:30px;height:30px}
.envelope .address{position:absolute;left:58px;top:50px;font-size:7px;color:var(--muted)}
.envelope-back{left:742px;top:670px;width:436px;height:226px}
.envelope-back .flap{position:absolute;left:0;top:0;width:100%;height:100%}
.envelope-back .site{position:absolute;left:0;top:30px;width:100%;text-align:center;font-size:10px;letter-spacing:4px;color:var(--blue-deep);font-weight:600}
</style>
</head>
<body>
<div class="canvas">

  <section class="sheet letterhead" aria-label="Letterhead">
    <div class="mark"><span class="mark-dot"></span>QUORVIX</div>
    <div class="tagline">Circuitry Supply Partners, LLC.</div>
    <ul class="contact-list">
      <li><i></i>457 Ridgeback Ave.</li>
      <li><i></i>Fernvale, QX 58204</li>
      <li><i></i>Phone 555-014-2233</li>
      <li><i></i>Fax 555-014-2234</li>
      <li><i></i>Mobile 555-014-2235</li>
      <li><i></i>mark@quorvix.com</li>
      <li><i></i>www.quorvix.com</li>
    </ul>
    <div class="watermark"></div>
    <svg class="band" viewBox="0 0 430 80" height="80" preserveAspectRatio="none">
      <path d="M0 26 Q215 -4 430 20 L430 80 L0 80Z" fill="#e6edf7"/>
      <path d="M0 34 Q215 6 430 26" fill="none" stroke="#1c2230" stroke-width="1.2"/>
      <defs><linearGradient id="g1" x1="0" x2="0" y1="0" y2="1"><stop offset="0" stop-color="#4a8df0"/><stop offset="1" stop-color="#0b3f9e"/></linearGradient></defs>
      <path d="M0 40 Q215 14 430 32 L430 80 L0 80Z" fill="url(#g1)"/>
    </svg>
    <div class="band-text">www.quorvix.com</div>
  </section>

  <section class="sheet folder" aria-label="Presentation folder">
    <div class="emblem"></div>
    <div class="name">QUORVIX</div>
    <div class="tagline">Circuitry Supply Partners, LLC.</div>
    <svg class="band" viewBox="0 0 425 90" height="90" preserveAspectRatio="none">
      <path d="M0 28 Q212 -4 425 22 L425 90 L0 90Z" fill="#e6edf7"/>
      <path d="M0 36 Q212 6 425 28" fill="none" stroke="#1c2230" stroke-width="1.2"/>
      <defs><linearGradient id="g2" x1="0" x2="0" y1="0" y2="1"><stop offset="0" stop-color="#4a8df0"/><stop offset="1" stop-color="#0b3f9e"/></linearGradient></defs>
      <path d="M0 44 Q212 16 425 36 L425 90 L0 90Z" fill="url(#g2)"/>
    </svg>
    <div class="band-text">www.quorvix.com</div>
  </section>

  <section class="sheet card card-front" aria-label="Business card front">
    <div class="mark"><span class="mark-dot"></span>QUORVIX</div>
    <div class="person"><strong>Paul Dunmore</strong>President</div>
    <div class="card-contact">
      P 555-014-2233<br>F 555-014-2234<br>mark@quorvix.com<br>457 Ridgeback Ave.
    </div>
    <svg class="band" viewBox="0 0 215 26" height="26" preserveAspectRatio="none">
      <path d="M0 10 Q107 0 215 6" fill="none" stroke="#1c2230" stroke-width=".8"/>
      <defs><linearGradient id="g3" x1="0" x2="0" y1="0" y2="1"><stop offset="0" stop-color="#4a8df0"/><stop offset="1" stop-color="#0b3f9e"/></linearGradient></defs>
      <path d="M0 13 Q107 3 215 9 L215 26 L0 26Z" fill="url(#g3)"/>
    </svg>
  </section>

  <section class="sheet card card-back" aria-label="Business card back">
    <div class="emblem"></div>
    <svg class="band" viewBox="0 0 215 26" height="26" preserveAspectRatio="none">
      <path d="M0 10 Q107 0 215 6" fill="none" stroke="#1c2230" stroke-width=".8"/>
      <defs><linearGradient id="g4" x1="0" x2="0" y1="0" y2="1"><stop offset="0" stop-color="#4a8df0"/><stop offset="1" stop-color="#0b3f9e"/></linearGradient></defs>
      <path d="M0 13 Q107 3 215 9 L215 26 L0 26Z" fill="url(#g4)"/>
    </svg>
    <div class="band-text">www.quorvix.com</div>
  </section>

  <section class="sheet envelope" aria-label="Envelope front">
    <div class="mark"><span class="mark-dot"></span>QUORVIX</div>
    <div class="address">457 Ridgeback Ave. Fernvale, QX 58204</div>
  </section>

  <section class="sheet envelope-back" aria-label="Envelope back">
    <svg class="flap" viewBox="0 0 436 226" preserveAspectRatio="none">
      <defs><linearGradient id="g5" x1="0" x2="0" y1="0" y2="1"><stop offset="0" stop-color="#4a8df0"/><stop offset="1" stop-color="#0b3f9e"/></linearGradient></defs>
      <path d="M0 0 L436 0 L436 78 Q218 40 0 78Z" fill="#f7f9fc"/>
      <path d="M0 78 Q218 40 436 78" fill="none" stroke="#1c2230" stroke-width="1"/>
      <path d="M0 84 Q218 48 436 84 L436 118 L218 150 L0 118Z" fill="url(#g5)"/>
      <path d="M0 118 L218 150 L436 118" fill="none" stroke="#d6dde8" stroke-width="1"/>
    </svg>
    <div class="site">www.quorvix.com</div>
  </section>

</div>
</body>
</html>
```